Letterhead Design for Law Firm

**Edit: I have added the photo of a bottom that I like.

------
We are looking for a re-design of our new letterhead. The letterhead is for a law firm and will be used for digital and traditionally printed correspondence.

Here are some suggestions:

- Please use colours are #8ec900 and simple black.
- Please do not use any type of "waves" at the bottom of the page. This is not in style at all.
- Please stay modern yet conservative.
- Please use font Segoe UI Light or similar if you can
- Avoid clipart or illustrations.
- Utilize ample white space in the layout so the design looks clean and information is easy to read at a glance. Don't overcrowd the letterhead.
- Make sure the letterhead design is consistent with our brand identity (see brambleford.ca)
-Please, no black headers or footers.

I am attaching my current letterhead and signature for your convenience.

Remember, the letterhead is an extension of our professional identity. We are a successful firm and trial lawyers who correspond with insurers, judges, lawyers, courts, clients, etc. Make it new, modern, attractive, yet powerful and conservative.

It needs to be easily printable. I would like the bleed removed in print so the black bar the bottom crosses the page (but the text is not near the edges)

Target Market(s)

Clients, Government Offices, Judiciary, Lawyers, Insurance Companies, Colleagues.

Industry/Entity Type

Law

Font styles to use
Other font styles liked:
• Segoe UI LIght, Calibri Light,

Colors
00AB8E
00BBA5
67D7C9
C6EFE9
E9F9F6

Requirements
Must have
• Everything that is on the letterhead now.
Nice to have
• Cutting Edge design, yet conservative.
Should not have
• law firm cliche design, images,

```html
<!DOCTYPE html>
<html lang="en">
<head>
<meta charset="utf-8">
<title>Brambleford Letterhead</title>
<link rel="stylesheet" href="https://fonts.googleapis.com/css2?family=Lato:wght@400;700&family=Questrial&family=Montserrat:wght@500;600&family=Open+Sans:wght@600&display=swap">
<style>
  :root {
    --green: #8ec900;
    --black: #0b0b0b;
    --ink: #1a1a1a;
    --body-grey: #7a7a7a;
    --rule: #d4d4d4;
    --backdrop: #ebebee;
    --paper: #ffffff;
  }
  * { box-sizing: border-box; margin: 0; padding: 0; }
  html, body { width: 1068px; height: 1200px; overflow: hidden; background: var(--backdrop); }
  .letterhead {
    position: absolute; left: 106px; top: 0;
    width: 855px; height: 1200px;
    background: var(--paper);
    color: var(--ink);
  }
  .firm-name {
    position: absolute; left: 47px; top: 78px;
    font-family: "Lato", sans-serif; font-weight: 400;
    font-size: 37px; letter-spacing: 1px; color: var(--black);
  }
  .contact {
    position: absolute; left: 389px; top: 48px;
    font-family: "Lato", sans-serif; font-size: 14px; line-height: 16.7px;
  }
  .contact .accent, .practice .accent { color: var(--green); }
  .practice {
    position: absolute; right: 47px; top: 48px; text-align: right;
    font-family: "Lato", sans-serif; font-size: 14px; line-height: 19.5px;
  }
  .practice .title { font-weight: 700; color: var(--green); }
  .header-rule {
    position: absolute; left: 47px; right: 47px; top: 196px;
    border-top: 1px solid var(--rule);
  }
  .recipient { position: absolute; left: 47px; top: 327px; font-family: "Questrial", sans-serif; }
  .recipient .name { font-family: "Montserrat", sans-serif; font-weight: 600; font-size: 26px; line-height: 30px; margin-bottom: 10px; }
  .recipient p { font-size: 14.5px; line-height: 20px; margin-bottom: 7px; }
  .recipient p.address { line-height: 20px; }
  .date {
    position: absolute; right: 40px; top: 449px;
    font-family: "Open Sans", sans-serif; font-weight: 600; font-size: 19px;
  }
  .body-copy {
    position: absolute; left: 47px; top: 504px; width: 768px;
    font-family: "Questrial", sans-serif; font-size: 19.5px; line-height: 26.4px;
    color: var(--body-grey); text-align: justify; hyphens: auto;
  }
  .body-copy p + p { margin-top: 27px; }
  .sign-off {
    position: absolute; left: 534px; top: 896px;
    font-family: "Montserrat", sans-serif; font-weight: 500; font-size: 22.5px;
  }
  .signature {
    position: absolute; left: 580px; top: 946px; width: 147px; height: 92px;
    background: linear-gradient(135deg, #f3f3f3, #e2e2e2);
  }
  .footer-bars { position: absolute; left: 48px; top: 1135px; }
</style>
</head>
<body>
  <main class="letterhead">
    <div class="firm-name">BRAMBLEFORD</div>

    <address class="contact" style="font-style:normal">
      <div>www.<span class="accent">BRAMBLEFORD</span>.ca</div>
      <div>48 Orchard Row, Suite 902</div>
      <div>Westbrook, ON&nbsp; K2M 4T7</div>
      <div><span class="accent">T:</span> 613-555-0142</div>
      <div><span class="accent">F:</span> 613-555-0187</div>
      <div><span class="accent">File Clerk:</span> Nora Whitfield</div>
      <div><span class="accent">Email:</span> nora@brambleford.ca</div>
    </address>

    <div class="practice">
      <div class="title">Practice Restricted</div>
      <div>Serious Personal Injury</div>
      <div>Wrongful Death Litigation</div>
      <div>Long-Term Disability Litigation</div>
      <div>Wrongful Dismissal Litigation</div>
      <div>Employee Terminations</div>
    </div>

    <div class="header-rule"></div>

    <section class="recipient">
      <div class="name">Jane Doe</div>
      <p>0123-456-789</p>
      <p>info@youremailaddress.com</p>
      <p class="address">1234 City Your Ln. Suite<br>123 Dallas, TX 0000</p>
    </section>

    <div class="date">12 December, 2024</div>

    <section class="body-copy">
      <p>Lorem ipsum dolor sit amet, consectetuer adipiscing elit, sed diam nonummy nibh euismod tincidunt ut laoreet dolore magna aliquam erat volutpat. Ut wisi enim ad minim veniam, quis nostrud exerci tation ullamcorper suscipit lobortis nisl ut aliquip ex ea commodo consequat. Duis autem vel eum iriure dolor in hendrerit in vulputate velit esse molestie consequat, vel illum dolore eu feugiat nulla facilisis at vero eros et accumsan et iusto odio dignissim qui blandit praesent luptatum zzril delenit augue duis dolore te feugait nulla facilisi.</p>
      <p>Lorem ipsum dolor sit amet, cons ectetuer adipiscing elit, sed diam nonummy nibh euismod tincidunt ut laoreet dolore magna aliquam erat volutpat. Ut wisi enim ad minim veniam, quis nostrud exerci tation ullamcorper suscipit lobortis nisl ut aliquip ex ea commodo consequat.</p>
    </section>

    <div class="sign-off">Mr. Daniel R. Ashcombe</div>
    <div class="signature" role="img" aria-label="Handwritten signature"></div>

    <svg class="footer-bars" width="764" height="10" viewBox="0 0 764 10" aria-hidden="true">
      <polygon points="0,0 392,0 385,9 0,9" fill="var(--black)"/>
      <polygon points="395,0 764,0 764,9 388,9" fill="var(--green)"/>
    </svg>
  </main>
</body>
</html>
```